Web Design Project

We need a logo, web site and business cards for our new business, Velquist Optics. We specialize in aerial videography and photography via drone. Currently we are mainly focusing on real estate videography but will branch into other markets and may even host training classes for flying drones.
Updates

Target Market(s)

Real estate agents, property managers, hotels and customers looking to learn how to fly drones.

Industry/Entity Type

Videography

Font styles to use
Sans Serif

Colors

Designer to choose colors to be used in the design.

Requirements
Must have
• Space for video feed on home page
A page for completed projects
A page for training classes
About us page

```html
<!DOCTYPE html>
<html lang="en">
<head>
<meta charset="utf-8">
<title>Velquist Optics</title>
<link rel="stylesheet" href="https://fonts.googleapis.com/css2?family=Cabin:wght@400;500;600&display=swap">
<style>
:root{
  --ink:#0b0b0b;
  --nav:#4a4a4a;
  --nav-line:#3a3a3a;
  --orange:#eda00e;
  --orange-dark:#d98a00;
  --text:#6a6a6a;
  --heading:#222;
  --footer:#474747;
  --white:#fff;
}
*{box-sizing:border-box;margin:0;padding:0}
html,body{width:747px;height:1200px;overflow:hidden;background:var(--white)}
body{position:relative;font-family:"Cabin",sans-serif;color:var(--text)}
.abs{position:absolute}
.site-header{left:0;top:0;width:747px;height:58px;background:var(--ink)}
.brand{left:74px;top:14px;display:flex;align-items:center;gap:8px;color:var(--white);font-size:20px;font-weight:600;letter-spacing:.5px}
.brand-mark{width:18px;height:18px;background:var(--orange)}
.search{left:493px;top:17px;width:177px;height:22px;background:#3b3b3b;color:#aaa;font-size:8px;padding:7px 7px}
.search svg{position:absolute;right:8px;top:5px}
.main-nav{left:0;top:58px;width:747px;height:32px;background:var(--nav);border-bottom:1px solid #333}
.main-nav a{position:absolute;top:0;height:32px;line-height:32px;text-align:center;color:var(--white);font-size:11px;font-weight:500;text-decoration:none;border-right:1px solid var(--nav-line)}
.main-nav a.active{background:linear-gradient(#f7b83a,var(--orange-dark));color:#222}
.hero{left:0;top:90px;width:747px;height:260px;background:linear-gradient(#9fb3c4 0%,#c9b9a4 40%,#e39d5b 70%,#3a2e2a 100%)}
.caption{left:88px;top:257px;width:570px;height:85px;background:rgba(90,80,75,.8);color:var(--white);text-align:center;font-size:11.5px;line-height:21px;padding:10px 16px}
.arrow{top:315px;width:20px;height:18px;background:var(--orange)}
.arrow svg{display:block;margin:4px auto}
.hero-shadow{left:120px;top:350px;width:507px;height:22px;background:radial-gradient(ellipse at top,rgba(0,0,0,.18),transparent 70%)}
h2{position:absolute;font-size:14px;font-weight:500;color:var(--heading);letter-spacing:.3px}
.card{top:408px;width:233px;height:249px;border:1px solid #ccc}
.card .thumb{position:absolute;left:5px;top:6px;width:222px;height:147px}
.play{position:absolute;left:6px;bottom:8px;background:rgba(20,20,20,.85);color:var(--white);font-size:8px;padding:3px 6px 3px 4px;display:flex;align-items:center;gap:4px;border-radius:2px}
.card h3{position:absolute;left:5px;top:164px;font-size:10px;font-weight:500;color:var(--orange)}
.card p{position:absolute;left:5px;top:187px;width:222px;font-size:7.3px;line-height:17.5px}
.training{left:0;top:689px;width:747px;height:149px;background:var(--orange)}
.training h2{left:74px;top:18px;color:var(--white)}
.training p{position:absolute;left:73px;top:56px;width:350px;font-size:7.2px;line-height:14px;color:var(--white)}
.training .photo{position:absolute;left:450px;top:0;width:224px;height:149px;background:linear-gradient(135deg,#e6eef0,#9fc9cc 60%,#5a6e74)}
.about p{position:absolute;left:74px;top:908px;width:340px;font-size:7.3px;line-height:14px}
.btn{left:74px;top:990px;width:76px;height:20px;background:#111;color:var(--white);font-size:7.5px;line-height:20px;text-align:center;border-radius:3px}
.news-item{left:483px;width:190px;font-size:7.3px;line-height:14px}
.news-item .date{color:var(--orange)}
.news-item .more{color:#222}
.site-footer{left:0;top:1049px;width:747px;height:119px;background:var(--footer)}
.footer-col{top:1066px;width:140px}
.footer-col h4{font-size:11px;font-weight:400;color:var(--orange);margin-bottom:8px}
.footer-col li{list-style:none;font-size:7.5px;color:var(--white);line-height:17.6px}
.legal{left:0;top:1168px;width:747px;height:32px;background:var(--ink);color:#ccc;font-size:7.5px;padding:12px 74px;word-spacing:1px}
.legal span{margin-right:7px}
</style>
</head>
<body>
<header class="site-header abs"></header>
<div class="brand abs"><span class="brand-mark"></span>Velquist Optics</div>
<div class="search abs">SEARCH
  <svg width="12" height="12" viewBox="0 0 12 12"><circle cx="4.5" cy="4.5" r="3.3" fill="none" stroke="#ddd" stroke-width="1.4"/><line x1="7" y1="7" x2="11" y2="11" stroke="#ddd" stroke-width="1.8"/></svg>
</div>
<nav class="main-nav abs">
  <a class="active" style="left:74px;width:64px">HOME</a>
  <a style="left:138px;width:87px">ABOUT US</a>
  <a style="left:225px;width:75px">VIDEOS</a>
  <a style="left:300px;width:148px">COMPLETED PROJECTS</a>
  <a style="left:448px;width:133px">TRAINING CLASSES</a>
  <a style="left:581px;width:96px;border-right:none">CONTACT US</a>
</nav>
<section class="hero abs" role="img" aria-label="Camera drone flying over a city skyline at sunset"></section>
<div class="caption abs">LOREM IPSUM DOLOR SIT AMET, CONSECTETUER ADIPISCING ELIT, SED DIAM NONUMMY NIBH EUIS-<br>MOD TINCIDUNT UT LAOREET</div>
<div class="arrow abs" style="left:349px"><svg width="6" height="10" viewBox="0 0 6 10"><polyline points="5,1 1,5 5,9" fill="none" stroke="#fff" stroke-width="1.3"/></svg></div>
<div class="arrow abs" style="left:376px"><svg width="6" height="10" viewBox="0 0 6 10"><polyline points="1,1 5,5 1,9" fill="none" stroke="#fff" stroke-width="1.3"/></svg></div>
<div class="hero-shadow abs"></div>

<h2 style="left:74px;top:371px">FEATURED WORKS</h2>
<article class="card abs" style="left:123px">
  <div class="thumb" role="img" aria-label="Aerial view of white townhomes beside a forest" style="background:linear-gradient(#4f6a3a 0%,#6e8a4e 30%,#d8d8d8 55%,#9aa58a 100%)">
    <div class="play"><svg width="10" height="10" viewBox="0 0 10 10"><circle cx="5" cy="5" r="4.4" fill="none" stroke="#fff"/><path d="M4 3l3 2-3 2z" fill="#fff"/></svg>PLAY VIDEO</div>
  </div>
  <h3>AUTUMN WOODS TOWNHOMES</h3>
  <p>Proin gravida nibh vel velit auctor aliquet. Aenean sollicitu-din, lorem quis bibendum auctor, nisi elit consequat ipsum, nec sagittis sem nibh id elituis sed odio sit amet nibh</p>
</article>
<article class="card abs" style="left:390px">
  <div class="thumb" role="img" aria-label="Two-storey beach house with garden and driveway" style="background:linear-gradient(#3d86d6 0%,#b8d3ea 25%,#d9cfb2 50%,#8a7a6a 75%,#b5b0a8 100%)">
    <div class="play"><svg width="10" height="10" viewBox="0 0 10 10"><circle cx="5" cy="5" r="4.4" fill="none" stroke="#fff"/><path d="M4 3l3 2-3 2z" fill="#fff"/></svg>PLAY VIDEO</div>
  </div>
  <h3>HOUSE ON THE BEACH</h3>
  <p>Proin gravida nibh vel velit auctor aliquet. Aenean sollicitu-din, lorem quis bibendum auctor, nisi elit consequat ipsum, nec sagittis sem nibh id elituis sed odio sit amet nibh</p>
</article>

<section class="training abs">
  <h2>TRAINING CLASSES</h2>
  <p>Proin gravida nibh vel velit auctor aliquet. Aenean sollicitudin, lorem quis bibendum auctor, nisi elit consequat ipsum, nec sagittis sem nibh id elit. Duis sed odio sit amet nibh vulputate cursus a sit amet mauris. Morbi accumsan ipsum velit. Nam nec tellus a odio tincidunt auctor a ornare odio. Sed non &nbsp;mauris vitae erat consequat auctor eu in elit.</p>
  <div class="photo" role="img" aria-label="Business team seated around a glass meeting table"></div>
</section>

<section class="about">
  <h2 style="left:74px;top:876px">ABOUT US</h2>
  <p>Proin gravida nibh vel velit auctor aliquet. Aenean sollicitudin, lorem quis bibendum auctor, nisi elit consequat ipsum, nec sagittis sem nibh id elit. Duis sed odio sit amet nibh vulputate cursus a sit amet mauris. Morbi accumsan ipsum velit. Nam nec tellus a odio tincidunt auctor a ornare odio. Sed non &nbsp;mauris vitae erat consequat auctor eu in elit. Cllaboris nisi ut aliquip ex ea commodo consequat.</p>
  <div class="btn abs">READ MORE</div>
</section>

<section class="news">
  <h2 style="left:483px;top:876px">LATEST NEWS</h2>
  <div class="news-item abs" style="top:902px"><div class="date">Sept 4, 2014</div>Proin gravida nibh vel velit auctor aliquet. Aenean sollicitudin, lorem quis bibendum auctor, nisi elit<div class="more">READ MORE</div></div>
  <div class="news-item abs" style="top:962px;left:484px"><div class="date">June 4, 2014</div>Proin gravida nibh vel velit auctor aliquet. Aenean sollicitudin, lorem quis bibendum auctor, nisi elit<div class="more">READ MORE</div></div>
</section>

<footer class="site-footer abs"></footer>
<div class="footer-col abs" style="left:74px"><h4>Main Links</h4><ul><li>Link here</li><li>Link here</li><li>Link here</li><li>Link here</li></ul></div>
<div class="footer-col abs" style="left:225px"><h4>Quick Link</h4><ul><li>Link here</li><li>Link here</li><li>Link here</li><li>Link here</li></ul></div>
<div class="footer-col abs" style="left:375px"><h4>Main Links</h4><ul><li>Link here</li><li>Link here</li><li>Link here</li><li>Link here</li></ul></div>
<div class="footer-col abs" style="left:526px"><h4>Quick Link</h4><ul><li>Link here</li><li>Link here</li><li>Link here</li><li>Link here</li></ul></div>
<div class="legal abs"><span>© Copyright 2014</span><span>Terms of Use</span><span>Privacy</span><span>Accessibility</span><span>Contact Us</span><span>Site Map</span></div>
</body>
</html>
```